Modernize Cleaning Chemical Product Labels

I am looking to modernise our product labels.
We are a cleaning chemical manufacture predominately in the commercial cleaning industry.
I would like for the labels to be available in at least 6 colours, red, green, blue, yellow, purple and orange.
Design can be as small as 270mm x 140mm up to 340mm x 165mm. Current label dimensions 275mm x 165mm
I have attached some of our current labels and our logo and also some competitors labels

Colors
0054AA
0677BA
7BADD7
CADEEF
E8F1F8
00AB8E
00BBA5
67D7C9
C6EFE9
E9F9F6
FFF300
FFF600
FEFA6F
FFFEC7
FFFEE8
F0912C
F2A743
F7CA91
FBE8D2
FDF5EE
EB3D1F
EC4F4E
F09395
F8D3D4
FCEDEE
A7469A
B969AE
D3A5CF
EDDBEB
F8F0F9

```html
<!DOCTYPE html>
<html lang="en">
<head>
<meta charset="utf-8">
<title>Halden Meridian Gleam – Final Rinse Aid Label</title>
<link rel="stylesheet" href="https://fonts.googleapis.com/css2?family=Archivo:wght@700;800&family=Archivo+Narrow:wght@700&family=Source+Serif+4:wght@400&display=swap">
<style>
  :root {
    --navy: #1f4a6e;
    --teal: #0ea0c9;
    --ink: #1f252c;
    --paper: #ffffff;
    --divider: #7badd7;
  }
  * { margin: 0; padding: 0; box-sizing: border-box; }
  html, body { width: 1200px; height: 720px; overflow: hidden; background: var(--paper); }
  .label {
    position: relative; width: 1200px; height: 720px; overflow: hidden;
    background: var(--paper); color: var(--ink);
    font-family: "Source Serif 4", Georgia, serif;
  }
  .frame { position: absolute; inset: 0; }
  .abs { position: absolute; }

  .brand-name {
    left: 0; width: 1200px; top: 26px; text-align: center;
    font-family: "Archivo", Arial, sans-serif; font-weight: 800;
    font-size: 50px; letter-spacing: 6px; color: var(--navy); line-height: 1;
  }

  .product-name {
    left: 0; width: 1200px; top: 215px; text-align: center;
    font-family: "Archivo", Arial, sans-serif; font-weight: 800;
    font-size: 66px; letter-spacing: 1px; color: var(--ink); line-height: 1;
    transform: scaleY(1.05);
  }
  .product-type {
    left: 0; width: 1200px; top: 289px; text-align: center;
    font-size: 41px; color: var(--teal); letter-spacing: 1.5px; line-height: 1;
  }
  .usage {
    left: 0; width: 1200px; top: 362px; text-align: center;
    font-family: "Archivo Narrow", Arial, sans-serif; font-weight: 700;
    font-size: 25px; line-height: 26px; color: var(--ink);
  }
  .benefits { left: 0; width: 1200px; top: 455px; list-style: none; }
  .benefits li {
    display: flex; justify-content: center; align-items: center; gap: 18px;
    font-size: 24px; line-height: 34.5px; letter-spacing: 0.5px; color: var(--ink);
  }
  .hex { width: 17px; height: 15px; flex: none; }

  .panel-heading {
    font-family: "Archivo", Arial, sans-serif; font-weight: 800;
    font-size: 16.5px; letter-spacing: 0.3px; color: var(--ink); line-height: 1;
  }
  .panel-copy {
    font-size: 9.6px; line-height: 11.8px; text-transform: uppercase; color: var(--ink);
  }
  .panel-copy.right { text-align: right; line-height: 12px; }
  .panel-copy.loose { line-height: 12.5px; }

  .warning-title {
    left: 0; width: 1200px; top: 600px; text-align: center;
    font-size: 33px; letter-spacing: 1.5px; color: var(--paper); line-height: 1;
  }
  .warning-list {
    list-style: none; color: var(--paper); font-size: 15.5px;
    line-height: 21.8px; letter-spacing: 0.4px;
  }
  .warning-list li::before { content: "•"; margin-right: 9px; }
  .warning-list.left { right: 600px; top: 641px; text-align: right; }
  .warning-list.right { left: 648px; top: 641px; }
  .warning-list .cont { padding-left: 14px; }
  .warning-list .cont::before { content: none; }
  .warning-divider { left: 623px; top: 647px; width: 3px; height: 56px; background: var(--divider); }
</style>
</head>
<body>
<main class="label">
  <svg class="frame" width="1200" height="720" viewBox="0 0 1200 720" aria-hidden="true">
    <!-- header bracket -->
    <polygon fill="var(--navy)" points="306,0 443,135 757,135 894,0 880,0 751,120 449,120 320,0"/>
    <!-- side brackets -->
    <polygon fill="var(--navy)" points="0,228 165,228 279,342 279,580 119,720 100,720 264,573 264,349 158,243 0,243"/>
    <polygon fill="var(--navy)" points="1200,228 1035,228 921,342 921,580 1081,720 1100,720 936,573 936,349 1042,243 1200,243"/>
    <!-- warning band -->
    <polygon fill="var(--navy)" points="303,591 897,591 1024,720 176,720"/>
    <!-- title rule -->
    <polygon fill="var(--ink)" points="426,346.5 600,345 774,346.5 600,348"/>
    <!-- hazard: exclamation -->
    <g transform="translate(116.5 90)">
      <rect x="-33" y="-33" width="66" height="66" transform="rotate(45)" fill="none" stroke="var(--navy)" stroke-width="6"/>
      <path d="M-6,-22 L6,-22 L3,8 L-3,8 Z" fill="var(--navy)"/>
      <circle cx="0" cy="15.5" r="5.5" fill="var(--navy)"/>
    </g>
    <!-- hazard: environment -->
    <g transform="translate(1083.5 91)">
      <rect x="-33" y="-33" width="66" height="66" transform="rotate(45)" fill="none" stroke="var(--navy)" stroke-width="6"/>
      <rect x="-20" y="-22" width="40" height="36" fill="var(--navy)" opacity="0.85" role="img" aria-label="Environmental hazard pictogram: dead tree and fish"/>
    </g>
  </svg>

  <div class="abs brand-name">HALDEN</div>

  <h1 class="abs product-name">MERIDIAN GLEAM</h1>
  <p class="abs product-type">FINAL RINSE AID</p>
  <p class="abs usage">FOR DOMESTIC AND<br>INDUSTRIAL DISHWASHERS</p>

  <ul class="abs benefits">
    <li><svg class="hex" viewBox="0 0 17 15"><polygon points="4,0 13,0 17,7.5 13,15 4,15 0,7.5" fill="var(--teal)"/></svg>Spot free, Clean Cutlery and Crockery<svg class="hex" viewBox="0 0 17 15"><polygon points="4,0 13,0 17,7.5 13,15 4,15 0,7.5" fill="var(--teal)"/></svg></li>
    <li><svg class="hex" viewBox="0 0 17 15"><polygon points="4,0 13,0 17,7.5 13,15 4,15 0,7.5" fill="var(--teal)"/></svg>Perfectly Clear Glassware<svg class="hex" viewBox="0 0 17 15"><polygon points="4,0 13,0 17,7.5 13,15 4,15 0,7.5" fill="var(--teal)"/></svg></li>
    <li><svg class="hex" viewBox="0 0 17 15"><polygon points="4,0 13,0 17,7.5 13,15 4,15 0,7.5" fill="var(--teal)"/></svg>Decreased Drying Time<svg class="hex" viewBox="0 0 17 15"><polygon points="4,0 13,0 17,7.5 13,15 4,15 0,7.5" fill="var(--teal)"/></svg></li>
  </ul>

  <!-- left panel -->
  <h2 class="abs panel-heading" style="left:19px; top:273px;">ALL THE LOREM</h2>
  <p class="abs panel-copy" style="left:19px; top:296px;">
    There are many variations<br>of passages of lorem ipsum<br>available, but the majority have<br>suffered alteration in some form,<br>by injected humour, or randomised<br>words which don't look even slightly<br>believable.<br>If you are going to use a passage<br>of lorem ipsum, you need to be sure<br>there isn't anything embarrassing<br>hidden in the middle of text.
  </p>
  <p class="abs panel-copy" style="left:19px; top:461px;">
    All the lorem ipsum generators on<br>the internet tend to repeat predefined<br>chunks as necessary, making this<br>the first true generator on the internet.
  </p>
  <h2 class="abs panel-heading" style="left:19px; top:530px;">HOW TO USE</h2>
  <p class="abs panel-copy" style="left:19px; top:548px; line-height:12px;">
    It uses a dictionary of over 200 latin<br>words, combined with a handful<br>of model sentence structures,<br>to generate lorem ipsum which<br>looks reasonable.<br>The generated lorem ipsum<br>is therefore always free from<br>repetition, injected humour,<br>or non-characteristic<br>words etc.
  </p>

  <!-- right panel -->
  <h2 class="abs panel-heading" style="left:997px; top:334px;">ALL THE LOREM</h2>
  <p class="abs panel-copy loose" style="left:965px; top:363px;">
    There are many variations<br>of passages of lorem ipsum<br>available, but the majority have<br>suffered alteration in some form,<br>by injected humour, or randomised<br>words which don't look even slightly<br>believable.<br>If you are going to use a passage<br>of lorem ipsum, you need to be sure<br>there isn't anything embarrassing<br>hidden in the middle of text.
  </p>
  <h2 class="abs panel-heading" style="left:1033px; top:530px;">HOW TO USE</h2>
  <p class="abs panel-copy right" style="right:15px; top:554px;">
    It uses a dictionary of over 200 latin<br>words, combined with a handful<br>of model sentence structures,<br>to generate lorem ipsum which<br>looks reasonable.<br>The generated lorem ipsum<br>is therefore always free from<br>repetition, injected humour,<br>or non-characteristic<br>words etc.
  </p>

  <!-- warning -->
  <h2 class="abs warning-title">WARNING</h2>
  <ul class="abs warning-list left">
    <li>NOT TO BE TAKEN</li>
    <li>KEEP OUT OF REACH OF CHILDREN</li>
    <li>READ SAFETY DIRECTIONS BEFORE OPENING</li>
  </ul>
  <div class="abs warning-divider"></div>
  <ul class="abs warning-list right">
    <li>CAUSES SERIOUS EYE IRRITATION</li>
    <li>TOXIC TO AQUATIQ LIFE WITH LONG</li>
    <li class="cont">LASTING EFFECTS</li>
  </ul>
</main>
</body>
</html>
```